Comic, writer, and entrepreneur based in Los Angeles, CA

UPDATED BRIEF:

Need a PROFESSIONAL yet simultaneously sexy business card that will inspire those to go to my social media accounts and follow me.

Need all of my social media (logos on card, please) As well as my picture, which I will provide.

If there is a way where you could scan the business card from your phone and it would take you to the social media accounts that would be great too!

My goal is to get a comedy writing job at the Nightly Desk or WLR and also go on Pelican Pond once my app is fully functional and created.

But the business card is just something to give people when I am making connections in both the entrepreneurial world as well as the comedy world so it has to help me stand out in that way :).

#: 417-552-8904
Email: kbellin@mx.ovrk.edu
Pictogram: Rosalind_Q.K
Chirpr: @ThePalermoNotes
Craftlo: Rosa’s Clever Tops (website: https://www.craftlo-example.com/shop/RosasTp?ref=pr_shop_more)
VidStream: The Gagmistress (website: https://www.vidstream-example.com/channel/QRpLwVn4kZ-mTHbyqo8erxt7B )
Friendlink: /rosalind.bellin.71924
Website App: WarmFixerFolk.example (app in progress. Need emails to make a prototype.)

Target Market(s)

Talent agents needing TV writers and TV comedy personalities. Investors for my app.

Industry/Entity Type

Tv

Contact Information for Business Card

Can be double or single sided, whichever looks best. Green is my favorite color but I am open to anything. Maybe silver and green?! Just make it classy and sexy.

Colors

Designer to choose colors to be used in the design.

Requirements
Must have
• Chirpr: ThePalermoNotes
• Pictogram: Rosalind_q.k
• Vidstream: The Gagmistress
• Email: kbellin@mx.ovrk.edu
• Phone: 417-552-8904
• writer, comic, entrepreneur--or--comedy writer and entrepeneur
Nice to have
• Make me standout. I'm a star ;-). Please check out my social media for files or ideas. Thanks.

```html
<!DOCTYPE html>
<html lang="en">
<head>
<meta charset="utf-8">
<title>Rosalind Bellin — Business Card</title>
<link rel="stylesheet" href="https://fonts.googleapis.com/css2?family=Exo:wght@500&family=Josefin+Sans:wght@400&display=swap">
<style>
  :root {
    --bg: #e9e7e3;
    --card-white: #f7f7f7;
    --card-black: #0b0b0b;
    --green: #6cc04a;
    --ink: #232323;
    --white: #ffffff;
    --photo-light: #bdbdbd;
    --photo-dark: #3a3a3a;
  }
  * { box-sizing: border-box; margin: 0; padding: 0; }
  html, body { width: 1200px; height: 800px; overflow: hidden; background: var(--bg); }
  .stage {
    width: 1200px; height: 800px;
    display: flex; flex-direction: column; align-items: center; justify-content: center; gap: 30px;
  }
  .card {
    position: relative; width: 600px; height: 343px; overflow: hidden;
    box-shadow: 0 6px 18px rgba(0,0,0,0.18);
    font-family: "Josefin Sans", sans-serif;
  }

  /* Back: social list */
  .card-back { background: var(--card-white); }
  .social-divider {
    position: absolute; left: 228px; top: 92px; width: 2px; height: 168px; background: var(--ink);
  }
  .social-list {
    position: absolute; left: 178px; top: 86px; list-style: none;
    display: flex; flex-direction: column; gap: 10px;
  }
  .social-item { display: flex; align-items: center; height: 26px; }
  .social-dot {
    width: 24px; height: 24px; border-radius: 50%; background: var(--green); flex: none;
  }
  .social-handle {
    margin-left: 46px; font-size: 17px; color: var(--ink); letter-spacing: 0.2px; white-space: nowrap;
  }

  /* Front: portrait + contact */
  .card-front { background: var(--card-black); }
  .front-shapes { position: absolute; inset: 0; }
  .identity {
    position: absolute; right: 40px; top: 110px; text-align: right;
  }
  .identity-name {
    font-family: "Exo", sans-serif; font-weight: 500; font-size: 30px; color: var(--green); line-height: 1;
  }
  .identity-role { margin-top: 8px; font-size: 17px; color: var(--white); }
  .contact-list {
    position: absolute; right: 26px; top: 222px; list-style: none; text-align: right;
    display: flex; flex-direction: column; gap: 8px;
  }
  .contact-item {
    display: flex; align-items: center; justify-content: flex-end; gap: 8px;
    font-size: 17px; color: var(--white); height: 22px;
  }
  .contact-icon { width: 16px; height: 16px; flex: none; }
</style>
</head>
<body>
<main class="stage">
  <section class="card card-back" aria-label="Card back: social channels">
    <div class="social-divider"></div>
    <ul class="social-list">
      <li class="social-item"><span class="social-dot"></span><span class="social-handle">Rosalind_Q.K</span></li>
      <li class="social-item"><span class="social-dot"></span><span class="social-handle">ThePalermoNotes</span></li>
      <li class="social-item"><span class="social-dot"></span><span class="social-handle">Rosa’s Clever Tops</span></li>
      <li class="social-item"><span class="social-dot"></span><span class="social-handle">The Gagmistress</span></li>
      <li class="social-item"><span class="social-dot"></span><span class="social-handle">rosalind.bellin.71924</span></li>
    </ul>
  </section>

  <section class="card card-front" aria-label="Card front: portrait and contact details">
    <svg class="front-shapes" width="600" height="343" viewBox="0 0 600 343">
      <defs>
        <linearGradient id="portrait-tone" x1="0" y1="0" x2="1" y2="1">
          <stop offset="0" stop-color="var(--photo-light)"/>
          <stop offset="1" stop-color="var(--photo-dark)"/>
        </linearGradient>
      </defs>
      <polygon class="portrait" role="img" aria-label="Black and white portrait photo of Rosalind Bellin"
               points="0,0 232,0 192,343 0,343" fill="url(#portrait-tone)"/>
      <polygon class="accent-top" points="232,0 372,0 212,170" fill="var(--green)"/>
      <polygon class="accent-bottom" points="205,232 192,343 300,343" fill="var(--green)"/>
      <line x1="232" y1="0" x2="192" y2="343" stroke="var(--white)" stroke-width="2"/>
    </svg>

    <div class="identity">
      <h1 class="identity-name">Rosalind Bellin</h1>
      <p class="identity-role">Writer, Comic, Entrepreneur</p>
    </div>

    <ul class="contact-list">
      <li class="contact-item">417-552-8904
        <svg class="contact-icon" viewBox="0 0 16 16" aria-hidden="true"><path d="M4 1.5l2.2 3-1.3 1.6c.8 1.8 2.2 3.3 4 4.1l1.6-1.3 3 2.2-1.2 2.7C7 13.5 2.5 9 1.5 3.3z" fill="var(--green)"/></svg>
      </li>
      <li class="contact-item">kbellin@mx.ovrk.edu
        <svg class="contact-icon" viewBox="0 0 16 16" aria-hidden="true"><rect x="1" y="3" width="14" height="10" fill="var(--green)"/><path d="M1.5 3.5L8 9l6.5-5.5" stroke="var(--card-black)" stroke-width="1.3" fill="none"/></svg>
      </li>
      <li class="contact-item">WarmFixerFolk.example
        <svg class="contact-icon" viewBox="0 0 16 16" aria-hidden="true"><g fill="none" stroke="var(--green)" stroke-width="1.4"><circle cx="8" cy="8" r="6.5"/><ellipse cx="8" cy="8" rx="2.8" ry="6.5"/><path d="M1.5 8h13M2.5 4.8h11M2.5 11.2h11"/></g></svg>
      </li>
    </ul>
  </section>
</main>
</body>
</html>
```